Truck wrap Halvik T-720 as a rolling billboard

have multiple trucks to wrap with logo and company info as a rolling billboard.

Tarnwell Outfitters logo

Main focus are in sod

contact 555-317-4486

licensed and insured - maybe on back of truck
"Sod and Landscape Installation and Delivery" - on side of truck

Target Market(s)

landscapers and builders

Industry/Entity Type

Landscape

Font styles to use
Sans Serif

Colors
acd037

Requirements
Must have
• photo of palletized sod
555-317-4486
Nice to have
• cool way to show palletized sod

Quenlar logo that can be added or taken away from deisgn
Should not have
• no big leaf
Sod needs to be bigger than the leaf from the logo

```html
<!DOCTYPE html>
<html lang="en">
<head>
<meta charset="utf-8">
<title>Tarnwell Outfitters – Halvik T-720 side wrap</title>
<link rel="stylesheet" href="https://fonts.googleapis.com/css2?family=Open+Sans:wght@400;600;700;800&display=swap">
<style>
  :root {
    --lime: #acd037;
    --lime-deep: #8cbc2a;
    --lime-wash: #e6f1c4;
    --orange: #f58a1f;
    --ink: #3b3b3b;
    --white: #ffffff;
    --stage: #f2f2f0;
  }
  html, body {
    margin: 0;
    width: 1200px;
    height: 927px;
    overflow: hidden;
    background: var(--stage);
    font-family: "Open Sans", Arial, sans-serif;
  }
  p { margin: 0; }
  .wrap-canvas {
    position: relative;
    width: 1200px;
    height: 927px;
  }
  .wrap-art {
    position: absolute;
    inset: 0;
  }
  .brand {
    position: absolute;
    left: 505px;
    top: 462px;
    display: flex;
    align-items: center;
    gap: 16px;
  }
  .brand-name {
    font-weight: 600;
    font-size: 30px;
    line-height: 1.05;
    color: var(--ink);
    font-variant: small-caps;
    letter-spacing: 0.5px;
  }
  .brand-dot {
    width: 32px;
    height: 32px;
    border-radius: 50%;
    background: var(--lime);
  }
  .tagline {
    position: absolute;
    left: 488px;
    top: 548px;
    font-weight: 700;
    font-size: 14px;
    color: var(--ink);
  }
  .phone {
    position: absolute;
    left: 478px;
    top: 582px;
    font-weight: 700;
    font-size: 44px;
    line-height: 1.1;
    color: var(--white);
    letter-spacing: 1px;
  }
  .sod-pallet {
    position: absolute;
    left: 830px;
    top: 412px;
    width: 222px;
    height: 228px;
    border-radius: 4px;
    background: linear-gradient(180deg, #6f9a3a 0%, #5b7f32 22%, #8a7a52 30%, #6b7a3c 55%, #8b7850 80%, #5e7a8a 100%);
  }
  .partner-mark {
    position: absolute;
    left: 1018px;
    top: 590px;
    color: var(--white);
    font-weight: 700;
    line-height: 1;
  }
  .partner-mark .parent {
    display: block;
    font-size: 9px;
    margin-bottom: 2px;
  }
  .partner-mark .name {
    font-size: 22px;
  }
</style>
</head>
<body>
<main class="wrap-canvas">
  <svg class="wrap-art" viewBox="0 0 1200 927" width="1200" height="927" aria-hidden="true">
    <defs>
      <clipPath id="panel-clip">
        <rect x="40" y="150" width="1120" height="620" rx="24"/>
      </clipPath>
    </defs>
    <rect x="40" y="150" width="1120" height="620" rx="24" fill="var(--white)"/>
    <g clip-path="url(#panel-clip)">
      <path class="orange-stripe" d="M40 448 C 220 430, 400 470, 600 600" fill="none" stroke="var(--orange)" stroke-width="12"/>
      <path class="lime-wash-band" d="M40 520 C 300 500, 600 540, 820 500 C 980 470, 1090 360, 1160 200 L1160 770 L40 770 Z" fill="var(--lime-wash)"/>
      <path class="lime-swoosh" d="M40 640 C 300 575, 560 575, 800 535 C 960 505, 1085 400, 1160 230 L1160 770 L40 770 Z" fill="var(--lime)"/>
      <path class="lime-body" d="M40 700 C 400 650, 800 640, 1160 560 L1160 770 L40 770 Z" fill="var(--lime-deep)" opacity="0.35"/>
      <path class="orange-stripe" d="M1110 150 C 1140 190, 1155 240, 1160 300" fill="none" stroke="var(--orange)" stroke-width="12"/>
    </g>
  </svg>

  <div class="brand">
    <span class="brand-name">Tarnwell<br>Outfitters</span>
    <span class="brand-dot"></span>
  </div>
  <p class="tagline">Sod and Landscape Installation and Delivery</p>
  <p class="phone">555-317-4486</p>

  <div class="sod-pallet" role="img" aria-label="Photo of a stacked pallet of fresh sod rolls"></div>

  <div class="partner-mark">
    <span class="parent">Ferrow</span>
    <span class="name">Quenlar</span>
  </div>
</main>
</body>
</html>
```